Diesel Fitting/Mechanical Company Needs a new Business Card

We would like a new business card that showcases our logo and business information.

Industry/Entity Type

Business

Contact Information for Business Card

314 Wendale Street
PO Box 7581 HOLLISVALE QLD 4873
Phone: 49312787 Fax: 49312688 Mobile: 0438915276 ABN: 63 519 087 342

Requirements
Must have
• The following email addresses:
• admin@tkservicing.com.au , sales@tkservicing.com.au , accounts@tkservicing.com.au , parts@tkservicing.com.au , office@tkservicing.com.au
• Also need to have the website: www.tkservicing.com.au

```html
<!DOCTYPE html>
<html lang="en">
<head>
<meta charset="utf-8">
<title>TK Servicing – Business Card</title>
<link rel="stylesheet" href="https://fonts.googleapis.com/css2?family=Questrial&display=swap">
<style>
  :root {
    --card-bg: #efefef;
    --ink: #3a3a3a;
    --ink-soft: #8d8d8d;
    --brand-orange: #f07a22;
    --accent-yellow: #f4b31c;
    --band-dark: #2a2a2a;
    --band-mid: #4a4a4a;
    --band-text: #ffffff;
    --rule: #c4c4c4;
    --icon-grey: #8a8a8a;
  }
  * { margin: 0; padding: 0; box-sizing: border-box; }
  html, body { width: 1200px; height: 741px; overflow: hidden; background: var(--card-bg); }
  body { font-family: "Questrial", "Century Gothic", sans-serif; color: var(--ink); }

  .card { position: relative; width: 1200px; height: 741px; background: var(--card-bg); overflow: hidden; }

  .corner-artwork { position: absolute; left: 0; top: 0; width: 440px; height: 440px; }

  .brand { position: absolute; right: 50px; top: 92px; text-align: right; }
  .brand-name { font-size: 66px; line-height: 1; color: var(--brand-orange); font-weight: 400; letter-spacing: 1px; }

  .website {
    position: absolute; right: 50px; top: 206px;
    font-size: 36px; letter-spacing: 1px; color: var(--ink-soft);
  }
  .website strong { color: var(--accent-yellow); font-weight: 400; }

  .phone-row {
    position: absolute; left: 222px; top: 348px; right: 50px;
    display: flex; align-items: center; justify-content: space-between;
    font-size: 36px; letter-spacing: 1px; color: var(--ink);
  }
  .phone-item { display: flex; align-items: center; gap: 14px; }
  .phone-item svg { width: 30px; height: 30px; fill: var(--icon-grey); }
  .phone-divider { width: 2px; height: 26px; background: var(--rule); }

  .email-band {
    position: absolute; left: 0; top: 427px; width: 1200px; height: 173px;
    background: radial-gradient(ellipse 420px 200px at 260px 110px, var(--band-mid), var(--band-dark) 80%);
  }
  .email-list {
    position: absolute; left: 238px; top: 14px;
    display: grid; grid-template-columns: 493px auto; row-gap: 9px;
    font-size: 31px; color: var(--band-text); list-style: none;
  }
  .email-list li { display: flex; align-items: center; gap: 16px; height: 40px; white-space: nowrap; }
  .email-list svg { width: 22px; height: 16px; flex: none; }

  .abn { position: absolute; right: 50px; top: 613px; font-size: 31px; color: var(--ink); }
  .address {
    position: absolute; right: 50px; top: 659px;
    display: flex; align-items: center; gap: 16px;
    font-size: 31px; font-style: normal; color: var(--ink); white-space: nowrap;
  }
  .address svg { width: 26px; height: 24px; fill: var(--icon-grey); }
</style>
</head>
<body>
<main class="card">

  <svg class="corner-artwork" viewBox="0 0 440 440" role="img" aria-label="Orange corner panel with interlocking machine gear decoration">
    <defs>
      <linearGradient id="cornerGlow" x1="0" y1="0" x2="1" y2="1">
        <stop offset="0" stop-color="#f06a1a"/>
        <stop offset="0.55" stop-color="#f58a22"/>
        <stop offset="1" stop-color="#f9a62a"/>
      </linearGradient>
    </defs>
    <polygon points="0,0 409,0 0,409" fill="url(#cornerGlow)"/>
    <line x1="424" y1="0" x2="0" y2="424" stroke="var(--brand-orange)" stroke-width="4"/>
    <line x1="6" y1="440" x2="36" y2="410" stroke="var(--brand-orange)" stroke-width="4"/>
  </svg>

  <header class="brand">
    <div class="brand-name">TK Servicing</div>
  </header>
  <div class="website">www.<strong>tkservicing</strong>.com.au</div>

  <section class="phone-row" aria-label="Phone numbers">
    <div class="phone-item">
      <svg viewBox="0 0 24 24" aria-label="Phone"><path d="M6.6 10.8a15.1 15.1 0 0 0 6.6 6.6l2.2-2.2a1 1 0 0 1 1-.25 11.4 11.4 0 0 0 3.6.57 1 1 0 0 1 1 1V20a1 1 0 0 1-1 1A17 17 0 0 1 3 4a1 1 0 0 1 1-1h3.5a1 1 0 0 1 1 1c0 1.25.2 2.45.57 3.57a1 1 0 0 1-.25 1z"/></svg>
      <span>49312787</span>
    </div>
    <span class="phone-divider"></span>
    <div class="phone-item">
      <svg viewBox="0 0 24 24" aria-label="Fax"><path d="M7 3h10v4H7zM4 8h16a2 2 0 0 1 2 2v6h-4v5H6v-5H2v-6a2 2 0 0 1 2-2zm4 8v3h8v-3z"/></svg>
      <span>49312688</span>
    </div>
    <span class="phone-divider"></span>
    <div class="phone-item">
      <svg viewBox="0 0 24 24" aria-label="Mobile"><path d="M8 1h8a2 2 0 0 1 2 2v18a2 2 0 0 1-2 2H8a2 2 0 0 1-2-2V3a2 2 0 0 1 2-2zm0 3v14h8V4zm4 15.5a1 1 0 1 0 0 2 1 1 0 0 0 0-2z"/></svg>
      <span>0438915276</span>
    </div>
  </section>

  <section class="email-band" aria-label="Email addresses">
    <ul class="email-list">
      <li><svg viewBox="0 0 22 16"><rect width="22" height="16" fill="var(--brand-orange)"/><path d="M1 1l10 8 10-8" stroke="#2a2a2a" stroke-width="2" fill="none"/></svg>admin@tkservicing.com.au</li>
      <li><svg viewBox="0 0 22 16"><rect width="22" height="16" fill="var(--brand-orange)"/><path d="M1 1l10 8 10-8" stroke="#2a2a2a" stroke-width="2" fill="none"/></svg>parts@tkservicing.com.au</li>
      <li><svg viewBox="0 0 22 16"><rect width="22" height="16" fill="var(--brand-orange)"/><path d="M1 1l10 8 10-8" stroke="#2a2a2a" stroke-width="2" fill="none"/></svg>sales@tkservicing.com.au</li>
      <li><svg viewBox="0 0 22 16"><rect width="22" height="16" fill="var(--brand-orange)"/><path d="M1 1l10 8 10-8" stroke="#2a2a2a" stroke-width="2" fill="none"/></svg>office@tkservicing.com.au</li>
      <li><svg viewBox="0 0 22 16"><rect width="22" height="16" fill="var(--brand-orange)"/><path d="M1 1l10 8 10-8" stroke="#2a2a2a" stroke-width="2" fill="none"/></svg>accounts@tkservicing.com.au</li>
    </ul>
  </section>

  <div class="abn">ABN: 63 519 087 342</div>
  <address class="address">
    <svg viewBox="0 0 26 24" aria-label="Address"><path d="M13 1l12 11h-4v11h-6v-7h-4v7H5V12H1z"/></svg>
    <span>314 Wendale Street PO Box 7581 Hollisvale QLD 4873</span>
  </address>

</main>
</body>
</html>
```